New Business Card for Casual Beachfront Cafe

Quirky Beachfront Cafe at Moana, South Australia needs a DOUBLE SIDED business card to print on PressLoom.

Target Market(s)

Business Cards sit on the counter for Guests to take with them. Please view our website www.saltwhistlekitchen.com.au to get a feel for the Cafe. You may also view our Instagram at @saltwhistlekitchen

Industry/Entity Type

Cafe / Restaurant

Contact Information for Business Card

Information equivalent to: Breakfast, Lunch, Dinner, Coffee, Takeaway / 87 Tidewater Parade Saltmere SA 5174 / Menu & Opening Hours: www.saltwhistlekitchen.com.au / ph (08) 8591 2736

Requirements
Must have
• Information equivalent to: Breakfast, Lunch, Dinner, Coffee, Takeaway / 87 Tidewater Parade Saltmere SA 5174 / Menu & Opening Hours: www.saltwhistlekitchen.com.au / ph (08) 8591 2736
Nice to have
• Potentially some of our trademark colours (Cafe can be searched via Trovix)
Should not have
• Must NOT have image of the building. May have the logo provided on one side but not necessarily, depending on how you wish to design the card

```html
<!DOCTYPE html>
<html lang="en">
<head>
<meta charset="utf-8">
<title>Salt Whistle Kitchen – Business Card</title>
<link href="https://fonts.googleapis.com/css2?family=Oswald:wght@500;700&family=Poppins:wght@400;700&display=swap" rel="stylesheet">
<style>
  :root {
    --navy: #12447f;
    --yellow: #ffff00;
    --rust: #c0591a;
    --white: #ffffff;
    --stage: #1f1f1f;
  }
  * { box-sizing: border-box; margin: 0; padding: 0; }
  html, body { width: 1200px; height: 1015px; overflow: hidden; background: var(--stage); }
  .stage { position: relative; width: 1200px; height: 1015px; }

  .card { position: absolute; left: 250px; width: 700px; height: 400px; overflow: hidden; }
  .card--back { top: 70px; background: var(--navy); }
  .card--front { top: 545px; background: var(--white); }

  /* back side */
  .hours {
    position: absolute; left: 140px; top: 40px; width: 400px; height: 275px;
    background: var(--yellow); color: var(--navy);
    font-family: "Poppins", sans-serif; text-align: center;
    display: flex; flex-direction: column; justify-content: center;
  }
  .hours__title { font-weight: 700; font-size: 20px; letter-spacing: .5px; }
  .hours__rule { width: 60px; height: 1px; background: var(--navy); margin: 4px auto 6px; }
  .hours__row { font-size: 18px; line-height: 1.3; }
  .hours__day { font-weight: 700; }

  .menu {
    position: absolute; left: 0; right: 0; bottom: 32px;
    display: flex; justify-content: center; align-items: center; gap: 16px;
    font-family: "Oswald", sans-serif; font-weight: 500; font-size: 22px;
    color: var(--white); letter-spacing: .5px;
  }
  .menu__dot { width: 8px; height: 8px; border-radius: 50%; background: var(--yellow); }

  /* front side */
  .block { position: absolute; background: var(--navy); }
  .block--top { left: 320px; top: 0; width: 150px; height: 110px; }
  .block--bottom { left: 470px; top: 275px; width: 150px; height: 125px; }

  .brand {
    position: absolute; left: 360px; top: 140px; width: 320px;
    display: flex; align-items: center; gap: 14px;
    font-family: "Oswald", sans-serif; font-weight: 700; font-size: 40px;
    line-height: 1; color: var(--navy); text-transform: uppercase;
  }
  .brand__mark { flex: none; width: 34px; height: 34px; background: var(--yellow); }

  .contact { position: absolute; left: 55px; top: 85px; list-style: none; }
  .contact__item { display: flex; align-items: center; gap: 22px; height: 82px; }
  .contact__icon {
    flex: none; width: 52px; height: 42px;
    background: var(--yellow); border: 3px solid var(--rust);
    display: flex; align-items: center; justify-content: center;
  }
  .contact__text {
    font-family: "Oswald", sans-serif; font-weight: 500; color: var(--navy);
    text-transform: uppercase; line-height: 1.1;
  }
  .contact__text--address { font-size: 21px; }
  .contact__text--phone { font-size: 32px; }
  .contact__text--web { font-size: 21px; }
</style>
</head>
<body>
<main class="stage">

  <section class="card card--back" aria-label="Card back">
    <div class="hours">
      <p class="hours__title">OPENING HOURS</p>
      <div class="hours__rule"></div>
      <p class="hours__row"><span class="hours__day">Mon</span> Closed</p>
      <p class="hours__row"><span class="hours__day">Tues</span> 8am-3pm</p>
      <p class="hours__row"><span class="hours__day">Wed</span> 8am-3pm, 5pm-9pm</p>
      <p class="hours__row"><span class="hours__day">Thur</span> 8am-3pm, 5pm-9pm</p>
      <p class="hours__row"><span class="hours__day">Fri</span> 8am-3pm, 5pm-9pm</p>
      <p class="hours__row"><span class="hours__day">Sat</span> 7:30am-9pm</p>
      <p class="hours__row"><span class="hours__day">Sun</span> 7:30am-4pm</p>
    </div>
    <p class="menu">
      <span>BREAKFAST</span><span class="menu__dot"></span>
      <span>LUNCH</span><span class="menu__dot"></span>
      <span>DINNER</span><span class="menu__dot"></span>
      <span>COFFEE</span><span class="menu__dot"></span>
      <span>TAKEAWAY</span>
    </p>
  </section>

  <section class="card card--front" aria-label="Card front">
    <div class="block block--top"></div>
    <div class="block block--bottom"></div>

    <div class="brand">
      <span class="brand__mark"></span>
      <span class="brand__name">Salt Whistle Kitchen</span>
    </div>

    <ul class="contact">
      <li class="contact__item">
        <span class="contact__icon">
          <svg width="18" height="22" viewBox="0 0 18 22" aria-hidden="true">
            <path d="M9 1a7 7 0 0 0-7 7c0 5 7 13 7 13s7-8 7-13a7 7 0 0 0-7-7z" fill="#12447f"/>
            <circle cx="9" cy="8" r="2.6" fill="#ffff00"/>
          </svg>
        </span>
        <span class="contact__text contact__text--address">87 Tidewater Parade<br>Saltmere SA 5174</span>
      </li>
      <li class="contact__item">
        <span class="contact__icon">
          <svg width="22" height="22" viewBox="0 0 24 24" aria-hidden="true">
            <path d="M6.6 10.8a15 15 0 0 0 6.6 6.6l2.2-2.2a1 1 0 0 1 1-.25 11.4 11.4 0 0 0 3.6.57 1 1 0 0 1 1 1V20a1 1 0 0 1-1 1A17 17 0 0 1 3 4a1 1 0 0 1 1-1h3.5a1 1 0 0 1 1 1c0 1.25.2 2.45.57 3.57a1 1 0 0 1-.25 1z" fill="#12447f"/>
          </svg>
        </span>
        <span class="contact__text contact__text--phone">(08) 8591 2736</span>
      </li>
      <li class="contact__item">
        <span class="contact__icon">
          <svg width="22" height="22" viewBox="0 0 24 24" aria-hidden="true" fill="none" stroke="#12447f" stroke-width="1.8">
            <circle cx="12" cy="12" r="9"/>
            <ellipse cx="12" cy="12" rx="4" ry="9"/>
            <path d="M3 12h18M4.5 7.5h15M4.5 16.5h15"/>
          </svg>
        </span>
        <span class="contact__text contact__text--web">www.saltwhistlekitchen.com.au</span>
      </li>
    </ul>
  </section>

</main>
</body>
</html>
```